Business Card Design for an Investment Company

We need a business card design for our private investment company, called Dunmore Equity. Dunmore Equity is an investments partnership that aims to acquire shares in listed companies with a view to influencing those companies through active dialogue in order to improve their value. We need designs that use the logo colors (blue, grey, white), we need both English and Arabic on the business cards (can be on one side or 2 sides). The final logo should communicate professionalism, conservatism (nothing too fancy or too cheesy), that we are smart, conservative and old school.

Target Market(s)

Investment companies

Industry/Entity Type

Investment

Contact Information for Business Card

Tariq Salmanuddin Farouqi
Senior Executive Officer

Harbor Court 07, Level 3, Office 214/12
QTFZ

+9714987650
tfarouqi@dunmore-equity.com
www.dunmore-equity.com

Requirements
Must have
• Logo to be placed on the left hand side of the business card
• for the Arabic, we only need to have the name and title so it can be accomodated on one side so we can have the other side with full color and logo. The arabic that needs to be used is the below:
• طارق سلمان الدين فاروقي
• المدير التنفيدي

```html
<!DOCTYPE html>
<html lang="en">
<head>
<meta charset="utf-8">
<title>Dunmore Equity – Business Card</title>
<link rel="stylesheet" href="https://fonts.googleapis.com/css2?family=Roboto:wght@400;500;700&family=Noto+Sans+Arabic:wght@400;500&display=swap">
<style>
  :root {
    --brand-blue: #156d9f;
    --brand-grey: #58585a;
    --text-grey: #4a4a4a;
    --rule-grey: #c9c9c9;
    --card-white: #ffffff;
    --backdrop: #e8e5e1;
  }
  * { margin: 0; padding: 0; box-sizing: border-box; }
  html, body {
    width: 1200px; height: 1000px; overflow: hidden;
    background: var(--backdrop);
    font-family: "Roboto", Arial, sans-serif;
  }
  .card {
    position: absolute; left: 269px; width: 662px;
    box-shadow: 0 3px 8px rgba(0,0,0,0.25);
  }
  .card-front {
    top: 108px; height: 378px;
    background: var(--brand-blue);
    color: var(--card-white);
  }
  .card-back {
    top: 521px; height: 380px;
    background: var(--card-white);
  }
  .wordmark {
    position: absolute; display: flex; align-items: center; gap: 10px;
    font-weight: 700; letter-spacing: -0.5px; white-space: nowrap;
  }
  .wordmark-square { display: inline-block; }
  .card-front .wordmark {
    left: 0; right: 0; top: 165px; justify-content: center;
    font-size: 46px; color: var(--card-white);
  }
  .card-front .wordmark-square { width: 14px; height: 14px; background: var(--card-white); }
  .website {
    position: absolute; left: 0; right: 0; top: 318px;
    text-align: center; font-size: 17px;
  }
  .card-back .wordmark {
    left: 36px; top: 36px; font-size: 38px; color: var(--brand-blue);
  }
  .card-back .wordmark-square { width: 12px; height: 12px; background: var(--brand-grey); }
  .identity { position: absolute; top: 189px; }
  .identity-en { left: 37px; }
  .identity-ar { right: 37px; text-align: right; font-family: "Noto Sans Arabic", Arial, sans-serif; direction: rtl; }
  .person-name { font-size: 17px; color: var(--brand-blue); line-height: 22px; }
  .person-title { font-size: 15px; color: var(--text-grey); line-height: 22px; }
  .identity-ar .person-name { font-size: 18px; line-height: 22px; }
  .identity-ar .person-title { font-size: 17px; }
  .contact-row {
    position: absolute; left: 37px; right: 37px;
    display: flex; justify-content: space-between; align-items: center;
    font-size: 15px; color: var(--text-grey);
  }
  .contact-row.phone { top: 262px; }
  .contact-row.email { top: 297px; }
  .contact-item { display: flex; align-items: center; gap: 5px; }
  .contact-item svg { fill: var(--brand-blue); }
  .contact-rule {
    position: absolute; left: 37px; right: 37px; top: 289px;
    height: 1px; background: var(--rule-grey);
  }
  .regulation {
    position: absolute; left: 0; right: 0; top: 349px;
    text-align: center; font-size: 11px; color: var(--text-grey);
  }
</style>
</head>
<body>
  <section class="card card-front">
    <div class="wordmark"><span class="wordmark-square"></span>Dunmore Equity</div>
    <div class="website">www.dunmore-equity.com</div>
  </section>

  <section class="card card-back">
    <div class="wordmark"><span class="wordmark-square"></span>Dunmore Equity</div>

    <div class="identity identity-en">
      <div class="person-name">Tariq Salmanuddin Farouqi</div>
      <div class="person-title">Senior Executive Officer</div>
    </div>
    <div class="identity identity-ar" lang="ar">
      <div class="person-name">طارق سلمان الدين فاروقي</div>
      <div class="person-title">المدير التنفيدي</div>
    </div>

    <div class="contact-row phone">
      <span class="contact-item">
        <svg width="11" height="11" viewBox="0 0 24 24" aria-hidden="true"><path d="M6.6 10.8a15.1 15.1 0 0 0 6.6 6.6l2.2-2.2a1 1 0 0 1 1-.25 11.4 11.4 0 0 0 3.6.57 1 1 0 0 1 1 1V20a1 1 0 0 1-1 1A17 17 0 0 1 3 4a1 1 0 0 1 1-1h3.5a1 1 0 0 1 1 1c0 1.25.2 2.45.57 3.57a1 1 0 0 1-.25 1z"/></svg>
        +9714987650
      </span>
      <span class="contact-item">Harbor Court 07, Level 3</span>
    </div>
    <div class="contact-rule"></div>
    <div class="contact-row email">
      <span class="contact-item">
        <svg width="11" height="9" viewBox="0 0 22 16" aria-hidden="true"><path d="M0 0h22v16H0z M1.5 1.5 11 9l9.5-7.5" fill="var(--brand-blue)"/><path d="M1 1l10 8 10-8" fill="none" stroke="#fff" stroke-width="1.6"/></svg>
        tfarouqi@dunmore-equity.com
      </span>
      <span class="contact-item">Office 214/12, QTFZ</span>
    </div>

    <div class="regulation">Regulated by the QFRA</div>
  </section>
</body>
</html>
```